Vantage Automotive Reconditioning Business Card

We need a professional business card that features our logo, a picture of the employee, and a brief list of our services.
I've attached a logo, and will attach photos at a later date.
The four services that need to be listed are Bumper repair and repainting, road rash repair, clear coat scratch repair, and automotive touch-up.
Target Market(s)
30 - 40 year male general managers of automobile dealerships. They are used to seeing every vendor gimmick under the sun. This brochure needs to impress with its simplicity and honesty.
Industry/Entity Type
Automotive
Look and feel
Each slider illustrates characteristics of the customer's brand and the style your logo design should communicate.

```html
<!DOCTYPE html>
<html lang="en">
<head>
<meta charset="utf-8">
<title>Vantage Automotive Reconditioning — Business Card</title>
<link rel="stylesheet" href="https://fonts.googleapis.com/css2?family=Montserrat:wght@400;500;700;800&display=swap">
<style>
  :root {
    --orange: #f15a24;
    --orange-deep: #e04e1b;
    --charcoal: #2b2b2b;
    --ink: #303030;
    --paper: #ffffff;
    --paper-shade: #f3f3f3;
    --backdrop-light: #d9d9d9;
    --backdrop-dark: #9a9a9a;
    --photo-top: #e6e8ee;
    --photo-bottom: #3a4fa8;
  }
  * { box-sizing: border-box; margin: 0; padding: 0; }
  html, body { width: 1200px; height: 900px; overflow: hidden; }
  body {
    background: radial-gradient(ellipse at 50% 35%, var(--backdrop-light), var(--backdrop-dark));
    font-family: "Montserrat", Arial, sans-serif;
    position: relative;
  }
  .card {
    position: absolute;
    left: 320px;
    width: 560px;
    height: 320px;
    background: linear-gradient(180deg, var(--paper), var(--paper-shade));
    overflow: hidden;
    box-shadow: 0 10px 24px rgba(0,0,0,0.25);
  }
  .card--front { top: 60px; }
  .card--back { top: 510px; }

  .wordmark {
    display: flex;
    align-items: center;
    gap: 12px;
    color: var(--charcoal);
    font-weight: 800;
    text-transform: uppercase;
    line-height: 1.05;
  }
  .wordmark__dot {
    width: 18px; height: 18px;
    border-radius: 50%;
    background: var(--orange);
    flex: none;
  }
  .wordmark__name { display: block; }

  /* Front */
  .card--front .wordmark {
    position: absolute;
    left: 120px; top: 80px;
    font-size: 30px;
    letter-spacing: 0.5px;
  }
  .card--front .wordmark__name small {
    display: block;
    font-size: 15px;
    letter-spacing: 1px;
  }
  .front-band {
    position: absolute;
    left: 0; right: 0; bottom: 0;
    height: 112px;
    background: var(--orange);
    border-top: 10px solid var(--charcoal);
  }
  .service-list {
    position: absolute;
    list-style: none;
    color: var(--paper);
    font-size: 12.5px;
    font-weight: 500;
    text-transform: uppercase;
    line-height: 1.6;
  }
  .service-list li::before {
    content: "";
    display: inline-block;
    width: 5px; height: 5px;
    border-radius: 50%;
    background: var(--charcoal);
    margin-right: 8px;
    vertical-align: middle;
  }
  .service-list--left { left: 40px; top: 28px; }
  .service-list--right { left: 310px; top: 28px; }

  /* Back */
  .card--back .wordmark {
    position: absolute;
    left: 28px; top: 60px;
    font-size: 24px;
    gap: 10px;
  }
  .card--back .wordmark__dot { width: 14px; height: 14px; }
  .card--back .wordmark__name small {
    display: block;
    font-size: 11px;
    letter-spacing: 0.8px;
  }
  .employee-photo {
    position: absolute;
    left: 318px; top: 0;
    width: 180px; height: 150px;
    background: linear-gradient(180deg, var(--photo-top) 30%, var(--photo-bottom));
  }
  .employee-name {
    position: absolute;
    left: 200px; top: 128px;
    color: var(--orange);
    font-size: 20px;
    font-weight: 500;
    text-transform: uppercase;
  }
  .back-band {
    position: absolute;
    left: 0; right: 0; top: 150px; bottom: 0;
    background: var(--orange);
    border-top: 8px solid var(--charcoal);
    border-bottom: 14px solid var(--charcoal);
  }
  .company-line {
    position: absolute;
    left: 200px; top: 14px;
    color: var(--paper);
    font-size: 13px;
    font-weight: 500;
    text-transform: uppercase;
  }
  .website {
    position: absolute;
    right: 30px; top: 40px;
    color: var(--paper);
    font-size: 14px;
  }
  .contact {
    position: absolute;
    left: 28px; top: 68px;
    color: var(--paper);
    font-size: 13px;
    line-height: 1.5;
    list-style: none;
  }
  .contact__title {
    font-weight: 700;
    text-transform: uppercase;
  }
  .contact li { display: flex; align-items: center; gap: 6px; }
  .contact svg { width: 14px; height: 14px; flex: none; }
  .contact__email { font-weight: 700; }
</style>
</head>
<body>

<section class="card card--front" aria-label="Business card front">
  <div class="wordmark">
    <span class="wordmark__dot"></span>
    <span class="wordmark__name">Vantage<small>Automotive Reconditioning</small></span>
  </div>
  <div class="front-band">
    <ul class="service-list service-list--left">
      <li>Bumper repair and repainting</li>
      <li>Road rash repair</li>
    </ul>
    <ul class="service-list service-list--right">
      <li>Clear coat scratch repair</li>
      <li>Automotive touch-up</li>
    </ul>
  </div>
</section>

<section class="card card--back" aria-label="Business card back">
  <div class="wordmark">
    <span class="wordmark__dot"></span>
    <span class="wordmark__name">Vantage<small>Automotive Reconditioning</small></span>
  </div>
  <div class="employee-photo" role="img" aria-label="Photo of the employee in blue work overalls holding a wrench"></div>
  <p class="employee-name">Marcus Hale</p>
  <div class="back-band">
    <p class="company-line">Vantage Automotive Reconditioning</p>
    <p class="website">www.vantageautorecon.com</p>
    <ul class="contact">
      <li class="contact__title">Vantage Automotive Reconditioning</li>
      <li>
        <svg viewBox="0 0 16 16" aria-hidden="true"><circle cx="8" cy="8" r="7.5" fill="#2b2b2b"/><path d="M5.2 4.2l1.6-.2.8 2-1 .8a5 5 0 0 0 2.6 2.6l.8-1 2 .8-.2 1.6c-3.8.4-7-2.8-6.6-6.6z" fill="#fff"/></svg>
        08 5550 0142
      </li>
      <li>
        <svg viewBox="0 0 16 16" aria-hidden="true"><circle cx="8" cy="8" r="7.5" fill="#2b2b2b"/><rect x="4.5" y="6" width="7" height="5" rx="1" fill="#fff"/><rect x="6" y="4" width="4" height="2.5" fill="#fff"/></svg>
        00 5550 0318
      </li>
      <li class="contact__email">
        <svg viewBox="0 0 16 16" aria-hidden="true"><circle cx="8" cy="8" r="7.5" fill="#2b2b2b"/><rect x="4" y="5" width="8" height="6" fill="#fff"/><path d="M4 5l4 3.5L12 5" fill="none" stroke="#2b2b2b" stroke-width="1"/></svg>
        marcushale@vantagemail.com
      </li>
    </ul>
  </div>
</section>

</body>
</html>
```